National Virtual CPA Firm needs post card design

Virtual CPA firm called "BRELLVO" needs a 5.5” x 8.5” post card designed to market our services to middle market mid-size american businesses. We provide Full Service Payroll (includes the processing of payroll, printing of checks and direct depositing, tax filing, and tax payments), Bookkeeping (Using their native systems, or ours), Contract CFO (with expense reduction analysis), Reporting services for business directors to make informed decisions, Capital Fundraising (Advice on seeking equity to help grow your business), and Taxes (Personal (1040), Partnership (1065), Corporate (1120, 1120S (Including Consolidated Returns)), Trust (1041) and Non-Profit (990)), including all affiliated state returns. One of our major selling points is our variety of experience, and our fast turn around times on projects.
This project specifically, I would like to highlight the bookkeeping services, but still want the tax and payroll services listed on the postcard.
I have uploaded the logo design for BRELLVO and would like a postcard that compliments the logo.
Company contact info is:
Brellvo accounting services Inc
P.O. Box 4638
Great falls, MT 59172
(800) 613-2794
Www.brellvo-example.com
Target Market(s)
Small to medium size businesses
Industry/Entity Type
Accounting
Look and feel

```html
<!DOCTYPE html>
<html lang="en">
<head>
<meta charset="utf-8">
<title>Brellvo Postcard</title>
<link rel="stylesheet" href="https://fonts.googleapis.com/css2?family=Oswald:wght@500&family=Tinos:wght@700&family=Arimo:wght@400;700&display=swap">
<style>
:root{
  --green:#3fae2a;
  --green-light:#6cc24a;
  --ink:#111111;
  --white:#ffffff;
  --paper:#f4f4f0;
  --yellow:#f5c400;
  --page:#ececec;
  --stamp:#eeeeee;
  --stamp-edge:#dddddd;
  --rule:#555555;
}
*{box-sizing:border-box;margin:0;padding:0}
html,body{width:1200px;height:2230px;overflow:hidden;background:var(--page)}
.card{position:absolute;left:50px;width:1100px;height:712px;background:var(--white);overflow:hidden;box-shadow:0 6px 18px rgba(0,0,0,.18)}
.card-front{top:330px;background:var(--paper)}
.card-back{top:1160px}
.layer{position:absolute;left:0;top:0;width:1100px;height:712px}
.photo{position:absolute;left:680px;top:0;width:420px;height:712px;background:linear-gradient(135deg,#d9e8cf 0%,#eef1ea 45%,#b9d6a6 100%)}
.brand{position:absolute;display:flex;align-items:center;gap:10px;font-family:"Tinos",serif;font-weight:700;color:var(--ink)}
.brand-dot{width:22px;height:22px;border-radius:50%;background:var(--yellow)}
.front-brand{left:44px;top:30px;font-size:32px}
.headline{position:absolute;left:50px;top:140px;font-family:"Oswald",sans-serif;font-weight:500;font-size:84px;line-height:92px;color:var(--green);text-transform:uppercase}
.headline-name{position:absolute;left:48px;top:340px;font-family:"Tinos",serif;font-weight:700;font-size:70px;color:var(--ink)}
.book-now{position:absolute;left:53px;top:466px;width:206px;height:38px;border-radius:19px;background:var(--yellow);display:flex;align-items:center;gap:12px;padding-left:28px;font-family:"Tinos",serif;font-weight:700;font-size:22px;color:var(--ink)}
.book-now svg{width:20px;height:20px}
.schedule{position:absolute;left:50px;top:524px;font-family:"Arimo",sans-serif;font-weight:700;font-size:24px;color:var(--ink)}
.front-web{position:absolute;left:50px;top:552px;font-family:"Arimo",sans-serif;font-weight:700;font-size:38px;color:var(--white)}
.call-label{position:absolute;left:50px;top:608px;font-family:"Arimo",sans-serif;font-weight:700;font-size:22px;color:var(--green-light)}
.front-phone{position:absolute;left:50px;top:636px;display:flex;align-items:center;gap:12px;font-family:"Tinos",serif;font-weight:700;font-size:46px;color:var(--white)}
.icon{flex:none}
.services-tag{position:absolute;left:0;top:53px;font-family:"Tinos",serif;font-weight:700;font-size:22px;color:var(--white);padding:6px 0 0 50px;width:340px;height:38px}
.service-list{position:absolute;left:44px;top:124px;width:500px;list-style:none;font-family:"Arimo",sans-serif;font-size:14.5px;line-height:18px;color:var(--white)}
.service-list li{display:flex;gap:10px;margin-bottom:16px}
.service-list svg{flex:none;margin-top:2px}
.back-contact{position:absolute;left:44px;font-family:"Arimo",sans-serif;font-weight:700;color:var(--white);display:flex;align-items:center;gap:14px}
.back-phone{top:570px;font-size:44px;font-family:"Tinos",serif}
.back-web{top:634px;font-size:38px}
.back-brand{left:624px;top:76px;font-size:26px}
.address{position:absolute;left:628px;top:134px;font-family:"Arimo",sans-serif;font-size:14.5px;line-height:19px;color:var(--ink);display:flex;gap:8px}
.stamp{position:absolute;left:917px;top:75px;width:126px;height:124px;background:var(--stamp);border:1px solid var(--stamp-edge)}
.address-line{position:absolute;left:701px;width:342px;height:2px;background:var(--rule)}
</style>
</head>
<body>

<section class="card card-front" aria-label="Postcard front">
  <div class="photo" role="img" aria-label="Photo of an accountant at a desk reviewing a printed bar chart"></div>
  <svg class="layer" viewBox="0 0 1100 712" aria-hidden="true">
    <path d="M600 0 L790 0 L765 40 L800 90 L750 140 L790 200 L735 260 L775 330 L720 390 L760 460 L710 520 L750 600 L700 660 L730 712 L640 712 L660 640 L625 560 L670 480 L630 400 L680 320 L640 240 L690 160 L650 80 Z" fill="var(--green)" opacity=".85"/>
    <path d="M0 516 L640 508 L700 530 L660 552 L720 575 L690 600 L610 612 L0 614 Z" fill="var(--green)"/>
    <path d="M0 598 L520 600 L610 590 L650 618 L600 640 L660 668 L610 690 L650 712 L0 712 Z" fill="var(--ink)"/>
  </svg>
  <div class="brand front-brand"><span class="brand-dot"></span>BRELLVO</div>
  <h1 class="headline">Virtual CPA<br>Firm Called</h1>
  <div class="headline-name">“BRELLVO”</div>
  <div class="book-now">Book Now
    <svg viewBox="0 0 20 20"><circle cx="10" cy="10" r="10" fill="var(--ink)"/><path d="M8 5 L13 10 L8 15" stroke="var(--white)" stroke-width="2.4" fill="none"/></svg>
  </div>
  <div class="schedule">SCHEDULE ONLLINE</div>
  <div class="front-web">www.brellvo-example.com</div>
  <div class="call-label">Call us now:</div>
  <div class="front-phone">
    <svg class="icon" width="36" height="36" viewBox="0 0 36 36"><circle cx="18" cy="18" r="18" fill="var(--yellow)"/><path d="M12 9 L16 9 L17 14 L14.5 16 Q17 21 20 22 L22 19.5 L27 21 L27 25 Q26 28 22 27 Q12 24 9 14 Q9 10 12 9 Z" fill="var(--ink)"/></svg>
    (800) 613-2794
  </div>
</section>

<section class="card card-back" aria-label="Postcard back">
  <svg class="layer" viewBox="0 0 1100 712" aria-hidden="true">
    <path d="M0 0 L530 0 L590 30 L560 70 L620 110 L580 160 L640 210 L600 260 L560 320 L610 380 L570 440 L600 500 L560 560 L0 560 Z" fill="var(--green)"/>
    <rect x="0" y="0" width="530" height="560" fill="var(--green-light)" opacity=".25"/>
    <path d="M0 53 L320 53 L340 71 L320 89 L0 89 Z" fill="var(--ink)"/>
    <path d="M0 540 L520 548 L590 530 L620 560 L570 600 L600 640 L560 680 L580 712 L0 712 Z" fill="var(--ink)"/>
  </svg>
  <div class="services-tag">We provide Full Service</div>
  <ul class="service-list">
    <li><svg width="14" height="14" viewBox="0 0 14 14"><rect x=".5" y=".5" width="13" height="13" fill="none" stroke="var(--yellow)"/><path d="M3 7 L6 10 L11 4" stroke="var(--yellow)" stroke-width="1.8" fill="none"/></svg><span>Payroll (includes the processing of payroll,<br>Printing of checks and direct depositing,<br>Tax filing,and tax payments),</span></li>
    <li><svg width="14" height="14" viewBox="0 0 14 14"><rect x=".5" y=".5" width="13" height="13" fill="none" stroke="var(--yellow)"/><path d="M3 7 L6 10 L11 4" stroke="var(--yellow)" stroke-width="1.8" fill="none"/></svg><span>Bookkeeping (Using their native systems, or ours),</span></li>
    <li><svg width="14" height="14" viewBox="0 0 14 14"><rect x=".5" y=".5" width="13" height="13" fill="none" stroke="var(--yellow)"/><path d="M3 7 L6 10 L11 4" stroke="var(--yellow)" stroke-width="1.8" fill="none"/></svg><span>Contract CFO (with expense reduction analysis),</span></li>
    <li><svg width="14" height="14" viewBox="0 0 14 14"><rect x=".5" y=".5" width="13" height="13" fill="none" stroke="var(--yellow)"/><path d="M3 7 L6 10 L11 4" stroke="var(--yellow)" stroke-width="1.8" fill="none"/></svg><span>Reporting services for business directors to make<br>informed decisions,</span></li>
    <li><svg width="14" height="14" viewBox="0 0 14 14"><rect x=".5" y=".5" width="13" height="13" fill="none" stroke="var(--yellow)"/><path d="M3 7 L6 10 L11 4" stroke="var(--yellow)" stroke-width="1.8" fill="none"/></svg><span>Capital Fundraising (Advice on seeking equity<br>to help grow your business),</span></li>
    <li><svg width="14" height="14" viewBox="0 0 14 14"><rect x=".5" y=".5" width="13" height="13" fill="none" stroke="var(--yellow)"/><path d="M3 7 L6 10 L11 4" stroke="var(--yellow)" stroke-width="1.8" fill="none"/></svg><span>And Taxes (Personal (1040),</span></li>
    <li><svg width="14" height="14" viewBox="0 0 14 14"><rect x=".5" y=".5" width="13" height="13" fill="none" stroke="var(--yellow)"/><path d="M3 7 L6 10 L11 4" stroke="var(--yellow)" stroke-width="1.8" fill="none"/></svg><span>Partnership (1065),</span></li>
    <li><svg width="14" height="14" viewBox="0 0 14 14"><rect x=".5" y=".5" width="13" height="13" fill="none" stroke="var(--yellow)"/><path d="M3 7 L6 10 L11 4" stroke="var(--yellow)" stroke-width="1.8" fill="none"/></svg><span>Corporate (1120, 1120S (Including Consolidated Returns)),</span></li>
    <li><svg width="14" height="14" viewBox="0 0 14 14"><rect x=".5" y=".5" width="13" height="13" fill="none" stroke="var(--yellow)"/><path d="M3 7 L6 10 L11 4" stroke="var(--yellow)" stroke-width="1.8" fill="none"/></svg><span>Trust (1041) and Non-Profit (990)),</span></li>
    <li><svg width="14" height="14" viewBox="0 0 14 14"><rect x=".5" y=".5" width="13" height="13" fill="none" stroke="var(--yellow)"/><path d="M3 7 L6 10 L11 4" stroke="var(--yellow)" stroke-width="1.8" fill="none"/></svg><span>Including all affiliated state returns</span></li>
  </ul>
  <div class="back-contact back-phone">
    <svg class="icon" width="32" height="32" viewBox="0 0 36 36"><circle cx="18" cy="18" r="18" fill="var(--yellow)"/><path d="M12 9 L16 9 L17 14 L14.5 16 Q17 21 20 22 L22 19.5 L27 21 L27 25 Q26 28 22 27 Q12 24 9 14 Q9 10 12 9 Z" fill="var(--ink)"/></svg>
    (800) 613-2794
  </div>
  <div class="back-contact back-web">
    <svg class="icon" width="32" height="32" viewBox="0 0 32 32"><circle cx="16" cy="16" r="16" fill="var(--yellow)"/><g stroke="var(--ink)" stroke-width="1.8" fill="none"><circle cx="16" cy="16" r="10"/><ellipse cx="16" cy="16" rx="4.5" ry="10"/><path d="M6 16 H26 M8 11 H24 M8 21 H24"/></g></svg>
    www.brellvo-example.com
  </div>

  <div class="brand back-brand"><span class="brand-dot"></span>BRELLVO</div>
  <div class="address">
    <svg width="12" height="16" viewBox="0 0 12 16"><path d="M6 0 A6 6 0 0 1 12 6 C12 10 6 16 6 16 C6 16 0 10 0 6 A6 6 0 0 1 6 0 Z" fill="var(--green)"/><circle cx="6" cy="6" r="2.2" fill="var(--white)"/></svg>
    <span>Brellvo accounting services Inc<br>P.O. Box 4638<br>Pell Harbor, MT 59172</span>
  </div>
  <div class="stamp"></div>
  <div class="address-line" style="top:378px"></div>
  <div class="address-line" style="top:442px"></div>
  <div class="address-line" style="top:506px"></div>
  <div class="address-line" style="top:571px"></div>
</section>

</body>
</html>
```